Nine Lanterns Quill House Book Cover for: "Growing Older Wisely"

We are a publishing company who plans to launch the book, Growing Older Wisely, A Handy Compact Manual for Legal, Financial and Emotional Health in late 2018. We desire a book cover that creates interest, looks professional and can draw readers to open and purchase this book. Growing Older Wisely is an invaluable, self-help book which provides Generation X, Baby Boomers and their families with the following information: steps to obtain valid, reliable wills and trusts, identify and pay for health care, address end of life care and manage grief. (Please see the attached book description for more information about the book contents). The cover needs to have a "wellness", health and healing emphasis but it should not be morbid. Instead, the cover should have an uplifting, inviting and engaging feeling.

The designer should use Photoshop to develop the 5 x 7 cover. Please design the front, back cover and spine using the attached suggested layout as a guide. Use colors that complement the background colors in the author's photo and the logo for the front and back colors. Feel free to change the colors of the black rectangles on the front of the book. We are looking for a design to be added using the suggested layouts but we are open to modifications of the layout provided that all the content in the attachments are used. Below are the specifications needed for the cover:

-Use Photoshop
-Develop a front and back cover for a 5 x 7 format book
-Include the book title, subtitle and author name on the front cover as noted on the front cover attachment
-Include a book title and author names on the spine of the cover
-Use full bleed background if appropriate
-Color correct and resize images as necessary
-Insert logo and publisher’s imprint on spine and back cover as noted in attachments

For designers who are successful with this contest, we will primarily consider you for future projects.

Thanks!

Target Market(s)

Generation X, Baby Boomers and their families

Industry/Entity Type

Book Publisher

Font styles to use
Sans Serif

Colors

Designer to choose colors to be used in the design.

Requirements
Must have
• The designer should use Photoshop to develop the 5 x 7 cover. Please design the front, back cover and spine using the attached suggested layout as a guide. Use colors that complement the background colors in the author's photo and the logo for the front and back colors. Feel free to change the colors of the black rectangles on the front of the book. We are looking for a design to be added using the suggested layouts but we are open to modifications of the layout provided that all the content in the attachments are used. Below are the specifications needed for the cover:
• -Use Photoshop
• -Develop a front and back cover for a 5 x 7 format book
• -Include the book title, subtitle and author name on the front cover as noted on the front cover attachment
• -Include a book title and author names on the spine of the cover
• -Use full bleed background if appropriate
• -Color correct and resize images as necessary
• -Insert logo and publisher’s imprint on spine and back cover as noted in attachments
Nice to have
• N/A
Should not have
• The design should not specifically duplicate the layout samples or include pictures of persons on the cover. We have provided those as a guide; we are looking for innovation and professionalism.

```html
<!DOCTYPE html>
<html lang="en">
<head>
<meta charset="utf-8">
<title>Growing Older Wisely – Book Cover</title>
<link rel="stylesheet" href="https://fonts.googleapis.com/css2?family=Cinzel:wght@400;500&family=EB+Garamond:wght@400;500&display=swap">
<style>
  :root {
    --paper: #ffffff;
    --ink: #141414;
    --rule: #2e3a33;
    --olive: #5b5c4a;
    --olive-light: #6d6e5b;
    --photo-tone: #4a5a4c;
    --box-line: #a9a9a9;
    --mark: #3a4694;
  }
  * { margin: 0; padding: 0; box-sizing: border-box; }
  html, body { width: 1200px; height: 764px; overflow: hidden; background: var(--paper); }
  .cover {
    position: relative;
    width: 1200px;
    height: 764px;
    background: var(--paper);
    color: var(--ink);
    font-family: "EB Garamond", Georgia, serif;
  }
  .display { font-family: "Cinzel", "Times New Roman", serif; font-weight: 400; }

  /* Back cover */
  .back-title {
    position: absolute; left: 60px; top: 38px; width: 414px;
    text-align: center; line-height: 1;
  }
  .back-title .line-small { display: block; font-size: 25px; letter-spacing: 0.02em; }
  .back-title .line-large { display: block; font-size: 54px; margin-top: 2px; }
  .back-subtitle {
    position: absolute; left: 56px; top: 140px; width: 422px;
    text-align: center; font-size: 13px; letter-spacing: 0.26em; line-height: 18px;
  }
  .back-copy {
    position: absolute; left: 60px; top: 190px; width: 414px;
    font-size: 13.2px; line-height: 16.4px; text-align: justify; hyphens: auto;
  }
  .back-copy p + p { margin-top: 16px; }
  .author-photo {
    position: absolute; left: 61px; top: 470px; width: 112px; height: 157px;
    background: linear-gradient(160deg, #6f7f6a 0%, var(--photo-tone) 55%, #2a2f3d 100%);
  }
  .author-bio {
    position: absolute; left: 182px; top: 469px; width: 292px;
    font-size: 10.6px; line-height: 14.4px; text-align: justify; hyphens: auto;
  }
  .isbn-box {
    position: absolute; left: 60px; top: 644px; width: 144px; height: 94px;
    border: 1px solid var(--box-line); background: var(--paper);
  }
  .imprint-name {
    position: absolute; left: 224px; top: 650px;
    font-size: 13px; letter-spacing: 0.02em; text-transform: uppercase;
  }
  .imprint-mark {
    position: absolute; left: 250px; top: 682px; width: 30px; height: 30px;
    background: var(--mark);
  }
  .imprint-web {
    position: absolute; left: 224px; top: 726px; font-size: 12.5px;
  }

  /* Spine */
  .spine-title {
    position: absolute; left: 560px; top: 48px; height: 270px;
    writing-mode: vertical-rl; line-height: 1; white-space: nowrap;
  }
  .spine-title .line-small { display: block; font-size: 27px; }
  .spine-title .line-large { display: block; font-size: 62px; }
  .spine-authors {
    position: absolute; left: 590px; top: 318px;
    writing-mode: vertical-rl; font-size: 15px; letter-spacing: 0.28em; white-space: nowrap;
  }
  .spine-mark {
    position: absolute; left: 585px; top: 668px; width: 30px; height: 30px;
    background: var(--mark);
  }

  /* Front cover */
  .front-rule {
    position: absolute; left: 702px; width: 448px; height: 4px; background: var(--rule);
  }
  .front-rule.top { top: 46px; }
  .front-rule.bottom { top: 232px; }
  .front-title {
    position: absolute; left: 702px; top: 62px; width: 448px; text-align: center; line-height: 1;
  }
  .front-title .line-small { display: block; font-size: 44px; letter-spacing: 0.01em; }
  .front-title .line-large { display: block; font-size: 92px; margin-top: 4px; letter-spacing: -0.01em; }
  .front-subtitle {
    position: absolute; left: 690px; top: 256px; width: 472px;
    text-align: center; font-size: 13px; letter-spacing: 0.28em; line-height: 18px;
  }
  .front-art {
    position: absolute; left: 788px; top: 336px; width: 364px; height: 296px;
    background: radial-gradient(ellipse at 35% 40%, var(--olive-light) 0%, var(--olive) 60%, #4b4c3d 100%);
    border-radius: 46% 40% 30% 45%;
  }
  .front-author {
    position: absolute; left: 690px; width: 472px; text-align: center; white-space: nowrap;
  }
  .front-author.primary { top: 670px; font-size: 30px; letter-spacing: 0.24em; }
  .front-author.contributor { top: 712px; font-size: 20px; letter-spacing: 0.22em; }
</style>
</head>
<body>
<main class="cover">

  <section class="back-cover">
    <h2 class="back-title display">
      <span class="line-small">GROWING OLDER</span>
      <span class="line-large">WISELY</span>
    </h2>
    <p class="back-subtitle display">A Handy Compact Manual for Legal,<br>Financial and Emotional Health</p>
    <div class="back-copy">
      <p>Death and taxes may be inevitable, but they both require a lot of preparation. Fifty percent of America’s seventy-four million baby boomers have parents eighty or older, and nearly half of those boomers haven’t discussed end-of-life issues with their loved ones.</p>
      <p>In Growing Older Wisely, the authors present a detailed, step-by-step guide on how to deal with aging. They tackle issues such as wills and trusts, estate planning, senior housing, caregiving, hospice care, and death and bereavement. Their approach is lighthearted but thorough, and they provide a sorely needed examination of all the details involved in growing old in America.</p>
      <p>Renata M. Hollis is a social services administrator, and Contributor Walter J. Ostrander is an attorney. They have combined their skills and knowledge to give readers a practical understanding of the issues involved in caring for an elderly family member.</p>
    </div>
    <div class="author-photo" role="img" aria-label="Portrait photograph of the author"></div>
    <p class="author-bio">Renata M. Hollis holds an advanced degree in Public Administration from Eastbrook State University and is currently an Administrator at the Westmoor County Office of Social Services. Collaborator Walter J. Ostrander is an attorney who has practiced for thirty-five years in the areas of family law, wills, trusts, and estate planning. In Growing Older Wisely, the two have pooled their expertise to provide an invaluable guide to all the issues involved in caring for a loved one at the end of his or her life.</p>
    <div class="isbn-box"></div>
    <p class="imprint-name">Nine Lanterns Quill House</p>
    <div class="imprint-mark"></div>
    <p class="imprint-web">www.renatahollisbooks.com</p>
  </section>

  <section class="spine">
    <h2 class="spine-title display">
      <span class="line-small">GROWING OLDER</span>
      <span class="line-large">WISELY</span>
    </h2>
    <p class="spine-authors display">HOLLIS WITH OSTRANDER</p>
    <div class="spine-mark"></div>
  </section>

  <section class="front-cover">
    <div class="front-rule top"></div>
    <h1 class="front-title display">
      <span class="line-small">GROWING OLDER</span>
      <span class="line-large">WISELY</span>
    </h1>
    <div class="front-rule bottom"></div>
    <p class="front-subtitle display">A Handy Compact Manual for Legal,<br>Financial and Emotional Health</p>
    <div class="front-art" role="img" aria-label="Illustration of a head in profile with target rings and a pointing hand touching the temple"></div>
    <p class="front-author primary display">RENATA M. HOLLIS</p>
    <p class="front-author contributor display">WALTER J. OSTRANDER</p>
  </section>

</main>
</body>
</html>
```